New signage for workshop frontage. Tarnell Welding & Repair is the company name. Looking for a cool font, metal fabrication is the trade. Also use TWAR as the logo

```html
<!DOCTYPE html>
<html lang="en">
<head>
<meta charset="utf-8">
<title>Tarnell Welding &amp; Repair – Workshop Sign</title>
<link rel="stylesheet" href="https://fonts.googleapis.com/css2?family=Roboto:ital,wght@0,700;0,900;1,700&family=Roboto+Condensed:wght@700&display=swap">
<style>
  :root {
    --backdrop: #e3e3e4;
    --sign-white: #ffffff;
    --brand-blue: #1379c3;
    --ink-black: #111214;
    --logo-ink: #23272d;
    --steel-light: #b9c2c8;
    --steel-dark: #5c6268;
  }
  * { margin: 0; padding: 0; box-sizing: border-box; }
  html, body {
    width: 1199px;
    height: 1200px;
    overflow: hidden;
    background: var(--backdrop);
  }
  .sign {
    position: absolute;
    left: 200px;
    top: 66px;
    width: 800px;
    height: 1067px;
    background: var(--sign-white);
    overflow: hidden;
    font-family: "Roboto", Arial, sans-serif;
  }
  .sign-shapes {
    position: absolute;
    inset: 0;
    width: 800px;
    height: 1067px;
  }
  .shape-blue { fill: var(--brand-blue); }
  .shape-black { fill: var(--ink-black); }

  .site-photo {
    position: absolute;
    left: 359px;
    top: 0;
    width: 441px;
    height: 311px;
    background: linear-gradient(160deg, var(--steel-light) 0%, #8d969c 45%, var(--steel-dark) 100%);
  }

  .brand-name {
    position: absolute;
    left: 62px;
    top: 62px;
    font-family: "Roboto", Arial, sans-serif;
    font-weight: 900;
    font-size: 92px;
    line-height: 1;
    letter-spacing: -1px;
    color: var(--logo-ink);
  }

  .headline-line {
    position: absolute;
    left: 62px;
    color: var(--sign-white);
    line-height: 1;
    white-space: nowrap;
  }
  .headline-lead {
    top: 454px;
    font-family: "Roboto", Arial, sans-serif;
    font-weight: 700;
    font-style: italic;
    font-size: 88px;
  }
  .headline-sub {
    font-family: "Roboto Condensed", "Arial Narrow", sans-serif;
    font-weight: 700;
    font-size: 72px;
  }
  .headline-sub.line-two { top: 549px; }
  .headline-sub.line-three { top: 624px; }

  .phone-icon {
    position: absolute;
    left: 58px;
    top: 966px;
    width: 46px;
    height: 46px;
  }
  .phone-number {
    position: absolute;
    left: 115px;
    top: 964px;
    font-family: "Roboto", Arial, sans-serif;
    font-weight: 700;
    font-size: 57px;
    line-height: 1;
    color: var(--sign-white);
    white-space: nowrap;
  }
</style>
</head>
<body>
  <main class="sign">
    <svg class="sign-shapes" viewBox="0 0 640 854" preserveAspectRatio="none" aria-hidden="true">
      <polygon class="shape-blue" points="0,184 537,184 537,647 410,740 0,646"/>
      <polygon class="shape-black" points="0,651 414,748 357,854 0,854"/>
      <polygon class="shape-blue" points="537,652 640,717 640,854 364,854 421,752"/>
    </svg>

    <div class="site-photo" role="img" aria-label="Photo of galvanised steel frame structure being fabricated inside an industrial plant, with a worker on a red scissor lift"></div>

    <div class="brand-name">TWAR</div>

    <h1 class="headline">
      <span class="headline-line headline-lead">TARNELL</span>
      <span class="headline-line headline-sub line-two">WELDING &amp;</span>
      <span class="headline-line headline-sub line-three">REPAIR</span>
    </h1>

    <svg class="phone-icon" viewBox="0 0 46 46" aria-hidden="true">
      <circle cx="23" cy="23" r="20.5" fill="none" stroke="#ffffff" stroke-width="3"/>
      <path d="M15.5 12.5c1.2-1 2.6-.8 3.3.4l2.1 3.6c.6 1 .3 2.2-.6 2.8l-1.4 1c.9 2.5 2.9 4.8 5.5 6l1.1-1.3c.7-.9 2-1.1 2.9-.4l3.4 2.4c1.1.8 1.2 2.3.2 3.3l-1.6 1.6c-1.3 1.3-3.3 1.6-5 .8-5.6-2.6-9.9-7.3-11.8-13.1-.6-1.8-.1-3.8 1.3-5z" fill="#ffffff"/>
    </svg>
    <div class="phone-number">1234 567 890</div>
  </main>
</body>
</html>
```